Business Card design for law firm = Juriskite Australia

We are seeking a new design for our business cards.
We are keeping our logo, which is attached.
We need space for
Name
Title
Address is , which is
Level 14
82 Penhallow Street
Sydney NSW 2000
Phone :
Mobile :
Fax :
Email :
DX :
website www.juriskite.com.au

Industry/Entity Type

Law Firm / Banking and Finance

Contact Information for Business Card

We are seeking a new design for our business cards. We are keeping our logo. We need space for Name Title Address is Level 14 82 Penhallow Street Sydney NSW 2000 Phone Mobile Fax Email DX website www.juriskite.com.au

Colors
0054AA
0677BA
7BADD7
CADEEF
E8F1F8

Requirements
Must have
• see our website for general feel www.juriskite.com.au

```html
<!DOCTYPE html>
<html lang="en">
<head>
<meta charset="utf-8">
<title>Juriskite Australia – Business Cards</title>
<link rel="stylesheet" href="https://fonts.googleapis.com/css2?family=Montserrat:wght@400;500;700&display=swap">
<style>
  :root {
    --bg: #8b9093;
    --card: #ffffff;
    --ink: #1f1d1e;
    --text: #2a2a2a;
    --blue: #0677ba;
    --blue-bright: #0a8fd1;
    --blue-light: #7badd7;
    --edge: #e4e6e8;
  }
  html, body {
    margin: 0;
    width: 1200px;
    height: 1000px;
    overflow: hidden;
    background: var(--bg);
    font-family: "Montserrat", Arial, sans-serif;
  }
  .canvas {
    position: relative;
    width: 1200px;
    height: 1000px;
  }
  .card {
    position: absolute;
    width: 540px;
    height: 330px;
    background: var(--card);
    overflow: hidden;
    box-shadow: 0 10px 24px rgba(0,0,0,.28);
  }
  .card--details { left: 70px; top: 120px; }
  .card--brand { left: 590px; top: 550px; }
  .card__shapes { position: absolute; inset: 0; }

  .brand {
    position: absolute;
    display: flex;
    flex-direction: column;
    align-items: flex-start;
  }
  .brand__name { color: var(--blue); font-weight: 500; letter-spacing: .5px; line-height: 1; }
  .brand__tagline { color: var(--blue-light); font-weight: 400; white-space: nowrap; }

  .card--details .brand { left: 392px; top: 74px; }
  .card--details .brand__name { font-size: 20px; color: var(--blue-bright); }
  .card--details .brand__tagline { margin-top: 6px; font-size: 8px; }

  .card--brand .brand { left: 170px; top: 134px; }
  .card--brand .brand__name { font-size: 44px; }
  .card--brand .brand__tagline { margin-top: 10px; margin-left: 4px; font-size: 15px; letter-spacing: .5px; }

  .person { position: absolute; left: 36px; top: 40px; }
  .person__name { margin: 0; color: var(--blue); font-weight: 700; font-size: 26px; letter-spacing: 1px; line-height: 1; }
  .person__title { margin: 4px 0 0; font-size: 9px; font-weight: 500; letter-spacing: .6px; color: var(--text); }
  .person__rule { width: 150px; height: 2px; background: var(--blue); margin-top: 5px; }
  .address { margin: 8px 0 0; font-size: 11px; line-height: 1.45; color: var(--text); font-style: normal; }

  .contacts { position: absolute; left: 36px; top: 168px; margin: 0; padding: 0; list-style: none; }
  .contacts li { display: flex; align-items: center; gap: 14px; height: 27px; font-size: 11.5px; color: var(--text); }
  .contacts .icon { width: 14px; height: 14px; flex: none; }
  .contacts .icon--dx { font-size: 10px; font-weight: 700; color: var(--blue); width: 14px; }
</style>
</head>
<body>
<main class="canvas">

  <section class="card card--details" aria-label="Business card, contact side">
    <svg class="card__shapes" width="540" height="330" viewBox="0 0 540 330" aria-hidden="true">
      <path d="M300 0 H330 L350 165 Q354 195 385 204 L540 250 V278 L378 230 Q326 215 320 170 Z" fill="var(--blue-bright)"/>
      <path d="M330 0 H540 V250 L385 204 Q354 195 350 165 Z" fill="var(--ink)"/>
    </svg>
    <div class="brand">
      <span class="brand__name">Juriskite</span>
      <span class="brand__tagline">strategic legal outsourcing</span>
    </div>

    <div class="person">
      <h1 class="person__name">NAME</h1>
      <p class="person__title">MANAGING DIRECTOR</p>
      <div class="person__rule"></div>
      <address class="address">Level 14, 82 Penhallow Street<br>Sydney NSW 2000</address>
    </div>

    <ul class="contacts">
      <li>
        <svg class="icon" viewBox="0 0 14 14" aria-label="Phone"><circle cx="7" cy="7" r="7" fill="var(--blue)"/><path d="M4.5 3.5 l1.4 0 .5 1.8 -.9.7 q.7 1.5 2.2 2.2 l.7-.9 1.8.5 0 1.4 q-4.2.3-5.7-5.7z" fill="#fff"/></svg>
        <span>02 8146 3270</span>
      </li>
      <li>
        <svg class="icon" viewBox="0 0 14 14" aria-label="Fax"><rect x="3.5" y="1.5" width="7" height="4" fill="var(--blue)"/><rect x="1" y="5" width="12" height="6" rx="1" fill="var(--blue)"/><rect x="3.5" y="9" width="7" height="4" fill="#fff" stroke="var(--blue)"/></svg>
        <span>02 8146 3271</span>
      </li>
      <li>
        <svg class="icon" viewBox="0 0 14 14" aria-label="Email"><rect x="1" y="3" width="12" height="8" rx="1" fill="var(--blue)"/><path d="M1.5 3.5 L7 7.5 L12.5 3.5" fill="none" stroke="#fff" stroke-width="1"/></svg>
        <span>enquiries@juriskite.com.au</span>
      </li>
      <li>
        <span class="icon icon--dx">DX</span>
        <span>318 Sydney</span>
      </li>
      <li>
        <svg class="icon" viewBox="0 0 14 14" aria-label="Website"><circle cx="7" cy="7" r="6" fill="none" stroke="var(--blue)" stroke-width="1.3"/><ellipse cx="7" cy="7" rx="2.6" ry="6" fill="none" stroke="var(--blue)" stroke-width="1"/><path d="M1 7 H13 M2 4 H12 M2 10 H12" stroke="var(--blue)" stroke-width="1"/></svg>
        <span>www.juriskite.com.au</span>
      </li>
    </ul>
  </section>

  <section class="card card--brand" aria-label="Business card, brand side">
    <svg class="card__shapes" width="540" height="330" viewBox="0 0 540 330" aria-hidden="true">
      <path d="M400 0 H540 V135 L505 128 Q480 122 472 95 Z" fill="var(--edge)"/>
      <path d="M420 0 H540 V118 L510 112 Q490 107 484 85 Z" fill="var(--ink)"/>
      <path d="M0 180 L40 185 Q70 190 80 220 L120 330 H0 Z" fill="var(--edge)"/>
      <path d="M0 198 L36 203 Q60 208 68 232 L100 330 H0 Z" fill="var(--ink)"/>
    </svg>
    <div class="brand">
      <span class="brand__name">Juriskite</span>
      <span class="brand__tagline">strategic legal outsourcing</span>
    </div>
  </section>

</main>
</body>
</html>
```